Telepsychology Services

The company is called 'Kestle' and it is a telehealth business.

I would like a lego which has some sort of telecommunications or health feel to it, with the message 'New Technology. New You' incoproated in it.

On the front side of the side I would like the logo with the message 'Providing psychological services to 'HARD-TO-KESTLE' INDIVIDUALS' printed in large font . I also need the message 'Real-time internet webcam conferencing' located on the front, along with the website address www.kestlemind.com.au.

On the backside of the card, I would appreicate the following information

Suitable for individuals
•living in remote areas of Australia,
•who experience impairment which leaves them housebound,
•with limited time availability for appointments, and
•for whom high levels of confidentiliaty are important

Designed for individuals with minimal or no webcam experience

Benefits provided by specific private health insurers, ie VORN

All Psychologists registered with the Southern Clinical Practice Oversight Bureau and members with the Federated Counselling Guild
Updates

Hi All,

Just a quick update.. I think I will prefer logos and busiiness cards that are relatively simple and understated. I am not a big fan of bright, multi colours and fancy designs. Just something clean, crisp, straightforward with a little colour ie blues and greens a good.

Also, for the back page, please keep in simple dot point form...

Thanks,

Mira

Industry/Entity Type

Telecommunications

Contact Information for Business Card

Kestle
www.kestlemind.com.au

```html
<!DOCTYPE html>
<html lang="en">
<head>
<meta charset="utf-8">
<title>Kestle Business Card</title>
<link rel="stylesheet" href="https://fonts.googleapis.com/css2?family=Arimo:wght@400&family=PT+Sans:wght@400&display=swap">
<style>
  :root {
    --stage: #ece8e2;
    --card-dark: #3b3b3d;
    --brand-green: #8dc63f;
    --text-light: #ffffff;
  }
  html, body {
    margin: 0;
    padding: 0;
    width: 1200px;
    height: 800px;
    overflow: hidden;
    background: var(--stage);
  }
  .canvas {
    position: relative;
    width: 1200px;
    height: 800px;
  }
  .card {
    position: absolute;
    top: 238px;
    width: 460px;
    height: 260px;
    border-radius: 10px;
    overflow: hidden;
    background: var(--card-dark);
  }
  .card--front { left: 110px; }
  .card--back { left: 592px; }
  .card__art {
    position: absolute;
    inset: 0;
    width: 460px;
    height: 260px;
  }
  .fill-green { fill: var(--brand-green); }
  .top-band {
    position: absolute;
    left: 0; top: 0;
    width: 100%;
    height: 30px;
    background: var(--brand-green);
  }
  .top-band__label {
    position: absolute;
    right: 24px;
    top: 3px;
    font: 400 17px/24px "PT Sans", sans-serif;
    color: var(--text-light);
  }
  .brand-name {
    position: absolute;
    left: 8px;
    top: 26px;
    margin: 0;
    font: 400 44px/50px "PT Sans", sans-serif;
    color: var(--text-light);
    letter-spacing: 0.5px;
  }
  .tagline {
    position: absolute;
    left: 38px;
    top: 85px;
    margin: 0;
    font: 400 15.5px/19px "Arimo", sans-serif;
    color: var(--text-light);
    text-transform: uppercase;
  }
  .service-line {
    position: absolute;
    left: 0;
    width: 396px;
    top: 204px;
    margin: 0;
    text-align: center;
    font: 400 14.5px/18px "Arimo", sans-serif;
    color: var(--brand-green);
    text-transform: uppercase;
  }
  .web-line {
    position: absolute;
    left: 0;
    width: 396px;
    top: 225px;
    margin: 0;
    text-align: center;
    font: 400 11px/14px "Arimo", sans-serif;
    color: var(--text-light);
  }
  .person {
    position: absolute;
    left: 110px;
    width: 304px;
    top: 74px;
    text-align: center;
  }
  .person__name {
    margin: 0;
    font: 400 28px/32px "Arimo", sans-serif;
    color: var(--brand-green);
  }
  .person__role {
    margin: 0;
    font: 400 13px/16px "Arimo", sans-serif;
    color: var(--text-light);
    letter-spacing: 0.3px;
  }
  .contact-list {
    position: absolute;
    left: 172px;
    top: 164px;
    margin: 0;
    padding: 0;
    list-style: none;
  }
  .contact-list__item {
    display: flex;
    align-items: center;
    height: 29px;
    font: 400 13px/16px "Arimo", sans-serif;
    color: var(--text-light);
  }
  .contact-list__icon {
    width: 16px;
    height: 16px;
    margin-right: 21px;
    fill: var(--brand-green);
  }
</style>
</head>
<body>
<main class="canvas">

  <section class="card card--front" aria-label="Card front">
    <svg class="card__art" viewBox="0 0 460 260" aria-hidden="true">
      <rect class="fill-green" x="0" y="141" width="355" height="5"/>
      <polygon class="fill-green" points="412,42 460,42 460,250 412,250 351,143"/>
    </svg>
    <div class="top-band"><span class="top-band__label">New Technology</span></div>
    <h1 class="brand-name">kestle</h1>
    <p class="tagline">Providing psychological services<br>to 'hard-to-Kestle' individuals'</p>
    <p class="service-line">Real-time internet webcam conferencing</p>
    <p class="web-line">www.kestlemind.com.au</p>
  </section>

  <section class="card card--back" aria-label="Card back">
    <svg class="card__art" viewBox="0 0 460 260" aria-hidden="true">
      <rect class="fill-green" x="105" y="141" width="355" height="5"/>
      <polygon class="fill-green" points="0,42 48,42 110,143 48,250 0,250"/>
    </svg>
    <div class="top-band"></div>
    <div class="person">
      <h2 class="person__name">Tomas Varlen</h2>
      <p class="person__role">DESIGNER</p>
    </div>
    <ul class="contact-list">
      <li class="contact-list__item">
        <svg class="contact-list__icon" viewBox="0 0 16 16" aria-hidden="true">
          <rect x="4" y="2" width="8" height="14" rx="1"/>
          <rect x="9" y="0" width="1.5" height="3"/>
          <rect x="5.5" y="4" width="5" height="4" fill="#3b3b3d"/>
          <rect x="5.5" y="9.5" width="1.3" height="1.3" fill="#3b3b3d"/>
          <rect x="7.4" y="9.5" width="1.3" height="1.3" fill="#3b3b3d"/>
          <rect x="9.2" y="9.5" width="1.3" height="1.3" fill="#3b3b3d"/>
          <rect x="5.5" y="12" width="1.3" height="1.3" fill="#3b3b3d"/>
          <rect x="7.4" y="12" width="1.3" height="1.3" fill="#3b3b3d"/>
          <rect x="9.2" y="12" width="1.3" height="1.3" fill="#3b3b3d"/>
        </svg>
        + 123 456 789
      </li>
      <li class="contact-list__item">
        <svg class="contact-list__icon" viewBox="0 0 16 16" aria-hidden="true">
          <rect x="1" y="3.5" width="14" height="9"/>
          <polyline points="1,3.5 8,9 15,3.5" fill="none" stroke="#3b3b3d" stroke-width="1.2"/>
        </svg>
        info@kestlemind.com.au
      </li>
      <li class="contact-list__item">
        <svg class="contact-list__icon" viewBox="0 0 16 16" aria-hidden="true">
          <circle cx="8" cy="8" r="7"/>
          <g fill="none" stroke="#3b3b3d" stroke-width="1">
            <ellipse cx="8" cy="8" rx="3" ry="7"/>
            <line x1="1" y1="8" x2="15" y2="8"/>
            <line x1="8" y1="1" x2="8" y2="15"/>
          </g>
        </svg>
        WWW.kestlemind.com.au
      </li>
    </ul>
  </section>

</main>
</body>
</html>
```